DILIGENCE COUNTS, OSRL, velmontsurety.net, New Infographic Design Project

Velmontsurety.net
Infographic
See attached information
Would like charts showing where funds from each bond goes

For design inspiration only, do not copy any of the elements - https://www.plorvexgallery.com/design/5820417

up coming Wardens summit! we would like something professional outlining our industries benefits to the justice process in Arkansas

see attached information. we would like similar graphics pie chart showing where money goes from each bond written etc.

Target Market(s)

Government law enforcement

Industry/Entity Type

Judicial

Requirements
Must have
• Professional graphics charts

```html
<!DOCTYPE html>
<html lang="en">
<head>
<meta charset="utf-8">
<title>OSRL – Arkansas Wardens' Summit</title>
<link rel="stylesheet" href="https://fonts.googleapis.com/css2?family=Bebas+Neue&family=Oswald:wght@500;700&family=Arimo:wght@400;700&display=swap">
<style>
:root{
  --navy:#22355f;
  --navy-dark:#172645;
  --red:#c32332;
  --white:#ffffff;
  --gray:#9aa0a8;
  --gray-light:#d3d6db;
  --ink:#4a4f57;
  --bg:#e9e9ea;
}
*{box-sizing:border-box;margin:0;padding:0}
html,body{width:1200px;height:800px;overflow:hidden;background:var(--bg)}
.flyer{position:absolute;left:294px;top:4px;width:612px;height:792px;background:var(--white);overflow:hidden;box-shadow:0 4px 18px rgba(0,0,0,.18);font-family:"Arimo",Arial,sans-serif}
.hero{position:absolute;left:0;top:0;width:612px;height:322px}
.hero svg{display:block}
.brand{position:absolute;left:26px;top:24px;display:flex;align-items:center;gap:8px;height:42px}
.brand-mark{width:22px;height:22px;background:var(--red)}
.brand-name{font-family:"Oswald",sans-serif;font-weight:700;color:var(--navy);font-size:40px;line-height:42px}
.brand-full{font-family:"Oswald",sans-serif;font-weight:700;color:var(--navy);font-size:13px;line-height:16px;position:absolute;left:62px;top:70px;white-space:nowrap}
.seal{position:absolute;right:32px;top:26px;width:66px;height:66px;border-radius:50%;background:var(--navy-dark);border:3px solid #c9a93e}
.event-title{position:absolute;right:22px;top:110px;text-align:right;font-family:"Bebas Neue",sans-serif;font-weight:400;color:var(--white);font-size:62px;line-height:60px;letter-spacing:.5px}
.intro{position:absolute;left:0;top:322px;width:612px;height:68px;background:var(--navy);color:var(--white);font-size:11.4px;line-height:14px;padding:11px 26px}
.rule-red{position:absolute;left:0;top:386px;width:612px;height:4px;background:var(--red)}
.rule-navy{position:absolute;left:0;top:392px;width:612px;height:2px;background:var(--navy)}
.bondsman-title{position:absolute;left:24px;top:404px;font-family:"Bebas Neue",sans-serif;font-weight:400;color:var(--navy);font-size:54px;line-height:50px}
.pie{position:absolute;left:318px;top:406px}
.pie-label{position:absolute;right:20px;font-size:9.5px;color:var(--navy)}
.divider{position:absolute;left:24px;top:518px;width:564px;height:1px;background:#dfe2e6}
.stat{position:absolute;top:530px;display:flex;gap:8px;align-items:center}
.stat-text{font-size:9.5px;line-height:13px;color:var(--gray)}
.stat-text b{color:var(--ink)}
.fees{position:absolute;left:0;top:602px;width:612px;height:190px;background:linear-gradient(180deg,#2e4470,#22355f)}
.fees-title{position:absolute;left:0;width:612px;top:14px;text-align:center;font-family:"Oswald",sans-serif;font-weight:500;color:var(--white);font-size:11px;letter-spacing:.3px}
.card{position:absolute;top:52px;width:102px;height:101px;background:var(--white);border-radius:3px;text-align:center;padding-top:44px;font-size:8.6px;line-height:12px}
.card-org{color:var(--red)}
.card-fee{color:var(--navy)}
.card-icon{position:absolute;left:29px;top:-20px;width:44px;height:44px;border-radius:50%;background:var(--navy);border:3px solid var(--white);display:flex;align-items:center;justify-content:center}
.total{position:absolute;left:106px;top:164px;width:404px;height:26px;background:var(--red);border-radius:13px 13px 0 0;color:var(--white);text-align:center;font-family:"Oswald",sans-serif;font-weight:500;font-size:11px;line-height:26px;letter-spacing:.3px}
</style>
</head>
<body>
<main class="flyer">
  <section class="hero">
    <svg width="612" height="322" viewBox="0 0 612 322">
      <defs>
        <linearGradient id="night" x1="0" y1="0" x2="1" y2="1">
          <stop offset="0" stop-color="#1d2a48"/>
          <stop offset=".55" stop-color="#3b4a66"/>
          <stop offset="1" stop-color="#1a2238"/>
        </linearGradient>
      </defs>
      <rect width="612" height="322" fill="url(#night)" role="img" aria-label="Night aerial photo of the Arkansas State Capitol and the Little Rock skyline"/>
      <path d="M0 0H612V22C520 18 440 40 360 82C270 128 140 126 0 104Z" fill="var(--navy)"/>
      <path d="M0 0H612V12C520 10 430 30 350 72C260 116 130 114 0 94Z" fill="var(--white)"/>
    </svg>
    <div class="brand"><span class="brand-name">osrl</span><span class="brand-mark"></span></div>
    <div class="brand-full">ozark surety &amp; release league</div>
    <div class="seal"></div>
    <h1 class="event-title">ARKANSAS<br>WARDENS'<br>SUMMIT</h1>
  </section>

  <p class="intro">Arkansas is one of the only states with a regulatory licensing board and an owner funded Association with a full-time lobbyist. We work with all law enforcement agencies to secure better legislation for Arkansas and the criminal justice system.</p>
  <div class="rule-red"></div><div class="rule-navy"></div>

  <h2 class="bondsman-title">TODAY'S BAIL<br>BONDSMAN</h2>
  <svg class="pie" width="290" height="110" viewBox="0 0 290 110">
    <path d="M119 61L119 79A78 30 0 0 1 2 53L2 35A78 30 0 0 0 119 61Z" fill="var(--navy-dark)"/>
    <path d="M158 35L158 53A78 30 0 0 1 119 79L119 61A78 30 0 0 0 158 35Z" fill="#6d737c"/>
    <path d="M80 35L119 61A78 30 0 1 1 119 9Z" fill="var(--navy)"/>
    <path d="M80 35L156.3 28.8A78 30 0 0 1 119 61Z" fill="var(--gray-light)"/>
    <path d="M80 35L119 9A78 30 0 0 1 156.3 28.8Z" fill="var(--gray)"/>
    <g stroke="#9aa0a8" stroke-width=".8" fill="#c5c9cf">
      <circle cx="135" cy="18" r="2"/><line x1="135" y1="18" x2="170" y2="4"/><line x1="170" y1="4" x2="280" y2="4"/>
      <circle cx="140" cy="38" r="2"/><line x1="140" y1="38" x2="170" y2="33"/><line x1="170" y1="33" x2="280" y2="33"/>
      <circle cx="110" cy="50" r="2"/><line x1="110" y1="50" x2="170" y2="68"/><line x1="170" y1="68" x2="280" y2="68"/>
    </g>
  </svg>
  <span class="pie-label" style="top:398px">$4.00 PER BOND</span>
  <span class="pie-label" style="top:427px">$6.00 PER BOND</span>
  <span class="pie-label" style="top:462px">$20.00 PER BOND</span>

  <div class="divider"></div>

  <div class="stat" style="left:26px">
    <svg width="58" height="58" viewBox="0 0 58 58"><circle cx="29" cy="29" r="27" fill="var(--gray-light)"/><circle cx="29" cy="29" r="13.5" fill="none" stroke="var(--navy)" stroke-width="27" stroke-dasharray="2 85" transform="rotate(-90 29 29)"/><text x="29" y="32" font-size="8" fill="var(--ink)" text-anchor="middle" font-family="Arimo,sans-serif">2.4%</text></svg>
    <p class="stat-text">Our industry maintains<br>a <b>2.4% FAILURE TO</b><br><b>APPEAR RATE</b></p>
  </div>
  <div class="stat" style="left:210px">
    <svg width="58" height="58" viewBox="0 0 58 58"><circle cx="29" cy="29" r="27" fill="var(--gray-light)"/><circle cx="29" cy="29" r="13.5" fill="none" stroke="var(--navy)" stroke-width="27" stroke-dasharray="34 85" transform="rotate(-90 29 29)"/><text x="40" y="20" font-size="8" fill="var(--white)" text-anchor="middle" font-family="Arimo,sans-serif">40%</text></svg>
    <p class="stat-text">All other forms of pre-trial<br>release average a <b>40%</b><br><b>FAILURE TO APPEAR</b><br><b>RATE</b></p>
  </div>
  <div class="stat" style="left:408px">
    <svg width="58" height="58" viewBox="0 0 58 58"><circle cx="29" cy="29" r="27" fill="var(--navy)"/><text x="29" y="32" font-size="8" fill="var(--white)" text-anchor="middle" font-family="Arimo,sans-serif">100%</text></svg>
    <p class="stat-text">We are <b>100%</b> responsible<br>for extradition fees on our<br>clients with no cost to the<br>taxpayer</p>
  </div>

  <section class="fees">
    <h3 class="fees-title">LEGISLATIVITY &nbsp;MANDATED FEES COLLECTED FOR EVERY BOND EXECUTED BY THE BONDSMAN</h3>

    <div class="card" style="left:24px">
      <span class="card-icon"><svg width="24" height="24" viewBox="0 0 24 24" fill="none" stroke="#fff" stroke-width="1.6"><path d="M3 8L12 3L21 8Z"/><path d="M6 10V18M10 10V18M14 10V18M18 10V18M3 21H21"/></svg></span>
      <p class="card-org">Arkansas wardens'<br>guild</p>
      <p class="card-fee">$6.00 per bond<br>100% of the budget</p>
    </div>
    <div class="card" style="left:140px">
      <span class="card-icon"><svg width="24" height="24" viewBox="0 0 24 24" fill="none" stroke="#fff" stroke-width="1.6"><circle cx="12" cy="8" r="4"/><path d="M4 21C4 15 20 15 20 21"/></svg></span>
      <p class="card-org">Arkansas public<br>counsel board</p>
      <p class="card-fee">$20.00 per bond<br>2/3 of their budget</p>
    </div>
    <div class="card" style="left:256px">
      <span class="card-icon"><svg width="24" height="24" viewBox="0 0 24 24" fill="none" stroke="#fff" stroke-width="1.6"><circle cx="7" cy="8" r="3"/><circle cx="17" cy="8" r="3"/><circle cx="12" cy="14" r="2.5"/><path d="M2 19C2 14 12 14 12 19C12 14 22 14 22 19"/></svg></span>
      <p class="card-org">Arkansas family<br>safety<br>commission</p>
      <p class="card-fee">$4.00 per bond</p>
    </div>
    <div class="card" style="left:372px">
      <span class="card-icon"><svg width="24" height="24" viewBox="0 0 24 24" fill="none" stroke="#fff" stroke-width="1.6"><path d="M12 3V20M7 20H17M4 6H20M4 6L1.5 13H6.5ZM20 6L17.5 13H22.5Z"/></svg></span>
      <p class="card-org">Bail bond recovery<br>fund (paid to the<br>county general fund)</p>
      <p class="card-fee">$4.00 per bond</p>
    </div>
    <div class="card" style="left:488px">
      <span class="card-icon"><svg width="24" height="24" viewBox="0 0 24 24" fill="none" stroke="#fff" stroke-width="1.6"><path d="M3 8L12 3L21 8Z"/><path d="M6 10V18M10 10V18M14 10V18M3 21H21"/><circle cx="19" cy="16" r="3"/></svg></span>
      <p class="card-org">State general<br>revenue and<br>agency operation</p>
      <p class="card-fee">$6.00 per bond</p>
    </div>

    <p class="total">TOTAL REVENUE GENERATED IN 2019 PRE-COVID $3,476,160.00</p>
  </section>
</main>
</body>
</html>
```